Torvane PowerPoint Template

I have a company called Torvane, LLC and my company logo is already designed. I need a PowerPoint template that I will be using to pitch potential investors and business partners. This should be a very professional-looking template that leverages the company logo colors and really pops. The company is an AI product research and development company.

```html
<!DOCTYPE html>
<html lang="en">
<head>
<meta charset="utf-8">
<title>Torvane Investor Presentation Template</title>
<link rel="stylesheet" href="https://fonts.googleapis.com/css2?family=Poppins:wght@300;400;500;600;700&display=swap">
<style>
:root{
  --red:#c1272d;
  --bright:#ff1414;
  --deep:#c80000;
  --dark:#4a4a4a;
  --ink:#3a3a3a;
  --blue:#a3c4e0;
  --paper:#ffffff;
  --mist:#efefef;
  --blush:#f7d9dc;
  --page:#000000;
}
*{margin:0;padding:0;box-sizing:border-box}
html,body{width:845px;height:1200px;overflow:hidden;background:var(--page)}
body{position:relative;font-family:'Poppins',sans-serif;color:var(--ink)}
.slide{position:absolute;width:327px;height:184px;overflow:hidden}
.frame{position:absolute;left:0;top:0;width:626px;height:352px;transform:scale(.5224);transform-origin:0 0;overflow:hidden}
.frame>svg.bg{position:absolute;left:0;top:0;width:626px;height:352px}
.abs{position:absolute}
.brand{position:absolute;display:flex;align-items:center;gap:10px}
.brand-dot{width:38px;height:38px;border-radius:50%;background:var(--red)}
.brand-name{font-weight:600;font-size:34px;letter-spacing:-.5px;color:var(--ink);line-height:1}
.lorem{font-size:10px;line-height:12.5px;font-weight:400}
.heading{font-weight:400;font-size:22px;letter-spacing:.5px}
/* positions */
.s1{left:79px;top:72px}.s2{left:439px;top:72px}
.s3{left:79px;top:286px}.s4{left:439px;top:286px}
.s5{left:79px;top:501px}.s6{left:439px;top:501px}
.s7{left:79px;top:715px}.s8{left:439px;top:715px}
.s9{left:79px;top:930px}.s10{left:439px;top:930px}

/* title slide */
.title-pill{left:35px;top:95px;width:275px;height:50px;border-radius:25px;background:linear-gradient(90deg,#fff 55%,rgba(255,255,255,0));padding-left:8px}
.title-pill .brand-dot{width:34px;height:34px}
.title-pill .brand-name{color:var(--red)}
.deck-title{left:40px;top:163px;color:#fff;font-weight:700;font-size:22px;line-height:29px}
.deck-sub{left:40px;top:225px;color:#fff;font-size:17px;font-weight:400}

/* agenda */
.agenda-label{left:390px;top:28px;color:#fff;font-size:22px}
.agenda-item{position:absolute;font-size:14.5px;color:var(--ink);padding-bottom:8px;border-bottom:1px solid #c9c9c9}

/* overview cards */
.card{position:absolute;left:118px;width:317px;height:62px;background:#fff;border-radius:6px}
.card-tab{position:absolute;left:17px;top:0;width:40px;height:46px;background:var(--bright);border-radius:0 0 20px 20px;color:#fff;font-size:20px;text-align:center;line-height:40px}
.card-dot{position:absolute;right:10px;top:8px;width:12px;height:12px;border-radius:50%;background:var(--blue)}
.card .lorem{position:absolute;left:75px;top:12px;width:215px;font-size:9px;line-height:12px}

/* market list */
.m-item{position:absolute;left:222px;display:flex;align-items:center;gap:20px}
.m-icon{width:32px;height:32px}
.m-item .lorem{width:290px}

/* swot */
.swot-col{position:absolute;top:85px;width:157px;height:267px;padding:22px 26px 0;color:#fff}
.swot-col h3{font-size:14.5px;font-weight:700;text-align:center;margin-bottom:18px;letter-spacing:.3px}
.swot-col p{font-size:10px;line-height:12.5px}

/* team */
.member{position:absolute;width:135px}
.member .role{font-size:8px;color:var(--red);font-weight:500}
.member .lorem{font-size:10px;line-height:12.5px}

/* thank you */
.thanks{left:257px;top:140px;width:225px;height:72px;border:1.5px solid #fff;border-radius:12px;color:#fff;font-weight:700;font-size:24px;display:flex;align-items:center;justify-content:center;letter-spacing:.5px}
</style>
</head>
<body>

<!-- 1 Title -->
<section class="slide s1"><div class="frame">
  <svg class="bg" viewBox="0 0 626 352">
    <defs><linearGradient id="handTone" x1="0" y1="0" x2="1" y2="1"><stop offset="0" stop-color="#dfe6ee"/><stop offset="1" stop-color="#9fb3c7"/></linearGradient></defs>
    <rect width="626" height="352" fill="var(--red)"/>
    <polygon points="430,0 626,0 626,190" fill="var(--dark)"/>
    <polygon points="0,0 90,0 0,90" fill="#b0242a"/>
    <polyline points="560,18 608,18 608,150" fill="none" stroke="var(--bright)" stroke-width="12"/>
    <circle cx="135" cy="345" r="62" fill="#d04a50"/>
    <polygon points="275,352 530,98 626,194 626,352" fill="var(--blue)"/>
    <rect x="440" y="200" width="186" height="130" fill="url(#handTone)" role="img" aria-label="Robotic hand holding a glowing AI chip"/>
  </svg>
  <div class="brand title-pill"><span class="brand-dot"></span><span class="brand-name">Torvane</span></div>
  <h1 class="abs deck-title">AI PRODUCT RESEARCH<br>&amp; DEVELOPMENT</h1>
  <p class="abs deck-sub">Investor Presentation</p>
</div></section>

<!-- 2 Agenda -->
<section class="slide s2"><div class="frame">
  <svg class="bg" viewBox="0 0 626 352">
    <rect width="626" height="352" fill="var(--mist)"/>
    <polygon points="0,145 0,352 212,352" fill="var(--blue)"/>
    <circle cx="70" cy="345" r="70" fill="#b3cde4"/>
    <polygon points="285,0 590,0 437,152" fill="none" stroke="var(--red)" stroke-width="1"/>
    <polygon points="300,0 575,0 437,138" fill="var(--red)"/>
    <polygon points="626,10 460,180 626,350" fill="var(--bright)"/>
    <polygon points="626,40 495,180 626,320" fill="var(--red)"/>
    <polygon points="626,70 525,180 626,290" fill="var(--dark)"/>
    <circle cx="640" cy="175" r="70" fill="#5e5e5e"/>
  </svg>
  <div class="brand" style="left:42px;top:35px"><span class="brand-dot"></span><span class="brand-name">Torvane</span></div>
  <p class="abs agenda-label">AGENDA</p>
  <p class="agenda-item" style="left:85px;top:104px">Company Overview</p>
  <p class="agenda-item" style="left:126px;top:144px">Problem &amp; Opportunity</p>
  <p class="agenda-item" style="left:172px;top:184px">Product Overview</p>
  <p class="agenda-item" style="left:206px;top:224px">Market &amp; Business Model</p>
  <p class="agenda-item" style="left:255px;top:264px">Team</p>
  <p class="agenda-item" style="left:301px;top:304px;border:0">Investment Ask</p>
</div></section>

<!-- 3 Company overview -->
<section class="slide s3"><div class="frame">
  <svg class="bg" viewBox="0 0 626 352">
    <rect width="626" height="352" fill="var(--blue)"/>
    <polygon points="0,0 40,0 97,52 0,150" fill="var(--dark)"/>
    <polygon points="0,0 25,0 75,50 0,125" fill="var(--bright)"/>
    <polygon points="0,0 10,0 52,48 0,100" fill="var(--red)"/>
    <circle cx="590" cy="60" r="60" fill="#b2cde4"/>
    <polygon points="455,352 626,186 626,352" fill="var(--dark)"/>
    <polygon points="510,352 626,238 626,262 535,352" fill="var(--bright)"/>
    <polygon points="555,352 626,282 626,310 583,352" fill="var(--red)"/>
  </svg>
  <p class="abs heading" style="left:118px;top:37px;color:#fff">COMPANY OVERVIEW</p>
  <div class="brand" style="left:415px;top:33px"><span class="brand-dot"></span><span class="brand-name">Torvane</span></div>
  <div class="card" style="top:103px"><span class="card-tab">A</span><span class="card-dot"></span><p class="lorem">Lorem ipsum dolor sit amet, elit dolor sit consectetuer adipiscing elit. Maecenas porttitor congue massa.</p></div>
  <div class="card" style="top:183px"><span class="card-tab">B</span><span class="card-dot"></span><p class="lorem">Lorem ipsum dolor sit amet, elit dolor sit consectetuer adipiscing elit. Maecenas porttitor congue massa.</p></div>
  <div class="card" style="top:263px"><span class="card-tab">C</span><span class="card-dot"></span><p class="lorem">Lorem ipsum dolor sit amet, elit dolor sit consectetuer adipiscing elit. Maecenas porttitor congue massa.</p></div>
</div></section>

<!-- 4 Product & services -->
<section class="slide s4"><div class="frame">
  <svg class="bg" viewBox="0 0 626 352">
    <defs><linearGradient id="circuitTone" x1="0" y1="0" x2="1" y2="0"><stop offset="0" stop-color="#0b2a5c"/><stop offset=".6" stop-color="#0a6fb8"/><stop offset="1" stop-color="#0a4a8f"/></linearGradient></defs>
    <rect width="626" height="352" fill="var(--paper)"/>
    <polygon points="0,0 245,0 0,245" fill="var(--blue)"/>
    <circle cx="42" cy="42" r="22" fill="none" stroke="#8fb5d6" stroke-width="6"/>
    <line x1="0" y1="250" x2="245" y2="0" stroke="var(--red)" stroke-width="6"/>
    <polygon points="235,24 626,24 626,153 118,153" fill="url(#circuitTone)" role="img" aria-label="Glowing blue circuit board pattern"/>
    <polygon points="0,352 115,190 275,352" fill="var(--blue)"/>
    <polygon points="0,352 0,330 115,218 250,352" fill="var(--bright)"/>
    <polygon points="20,352 115,248 220,352" fill="var(--red)"/>
    <polygon points="48,352 115,278 190,352" fill="var(--dark)"/>
  </svg>
  <div class="brand" style="left:415px;top:190px"><span class="brand-dot"></span><span class="brand-name">Torvane</span></div>
  <p class="abs heading" style="right:30px;top:262px;color:var(--ink)">PRODUCT &amp; SERVICES</p>
  <p class="abs lorem" style="right:30px;top:297px;width:290px;text-align:right;font-size:9.5px;line-height:12px">Lorem ipsum dolor sit amet, elit dolor sit consectetuer adipiscing elit. Maecenas porttitor congue massa.</p>
</div></section>

<!-- 5 Market opportunities list -->
<section class="slide s5"><div class="frame">
  <svg class="bg" viewBox="0 0 626 352">
    <rect width="626" height="352" fill="var(--paper)"/>
    <circle cx="580" cy="55" r="75" fill="var(--blush)"/>
    <circle cx="598" cy="32" r="20" fill="#fff" stroke="#f2c3c8" stroke-width="5"/>
    <path d="M0,175 L0,15 A160,160 0 0 1 94,45.6 Z" fill="var(--blue)"/>
    <path d="M0,175 L94,45.6 A160,160 0 0 1 152,125.6 Z" fill="var(--bright)"/>
    <path d="M0,175 L152,125.6 A160,160 0 0 1 152,224.4 Z" fill="var(--red)"/>
    <path d="M0,175 L152,224.4 A160,160 0 0 1 94,304.4 Z" fill="var(--dark)"/>
    <path d="M0,175 L94,304.4 A160,160 0 0 1 0,335 Z" fill="var(--blue)"/>
    <circle cx="0" cy="175" r="65" fill="#fff"/>
    <circle cx="0" cy="175" r="10" fill="var(--bright)"/>
    <g fill="#fff">
      <circle cx="36" cy="62" r="11"/>
      <rect x="84" y="100" width="26" height="6" rx="2"/><rect x="84" y="109" width="26" height="6" rx="2"/><rect x="84" y="118" width="26" height="6" rx="2"/>
      <rect x="100" y="172" width="4" height="18"/><rect x="107" y="178" width="4" height="12"/><rect x="114" y="168" width="4" height="22"/><rect x="121" y="180" width="4" height="10"/><rect x="98" y="190" width="30" height="2"/>
      <polygon points="84,237 97,230 110,237"/><rect x="86" y="239" width="3" height="14"/><rect x="92" y="239" width="3" height="14"/><rect x="99" y="239" width="3" height="14"/><rect x="105" y="239" width="3" height="14"/><rect x="83" y="254" width="28" height="3"/>
    </g>
    <g fill="none" stroke="#fff" stroke-width="3"><circle cx="36" cy="292" r="11"/><circle cx="36" cy="292" r="5"/></g>
  </svg>
  <div class="brand" style="left:222px;top:30px"><span class="brand-dot"></span><span class="brand-name">Torvane</span></div>
  <p class="abs heading" style="left:222px;top:80px">MARKET OPPERTUNITIES</p>
  <div class="m-item" style="top:112px"><svg class="m-icon" viewBox="0 0 32 32"><circle cx="16" cy="14" r="10" fill="var(--blue)"/><rect x="12" y="22" width="8" height="8" fill="var(--blue)"/></svg><p class="lorem">Lorem ipsum dolor sit amet, elit dolor sit consectetuer adipiscing elit. Maecenas porttitor congue massa.</p></div>
  <div class="m-item" style="top:156px"><svg class="m-icon" viewBox="0 0 32 32"><g fill="var(--blue)"><rect x="3" y="6" width="26" height="6" rx="2"/><rect x="3" y="14" width="26" height="6" rx="2"/><rect x="3" y="22" width="26" height="6" rx="2"/></g></svg><p class="lorem">Lorem ipsum dolor sit amet, elit dolor sit consectetuer adipiscing elit. Maecenas porttitor congue massa.</p></div>
  <div class="m-item" style="top:200px"><svg class="m-icon" viewBox="0 0 32 32"><g fill="var(--blue)"><rect x="5" y="8" width="4" height="20"/><rect x="12" y="14" width="4" height="14"/><rect x="19" y="5" width="4" height="23"/><rect x="26" y="17" width="4" height="11"/><rect x="2" y="28" width="29" height="2"/></g></svg><p class="lorem">Lorem ipsum dolor sit amet, elit dolor sit consectetuer adipiscing elit. Maecenas porttitor congue massa.</p></div>
  <div class="m-item" style="top:244px"><svg class="m-icon" viewBox="0 0 32 32"><g fill="var(--blue)"><polygon points="2,10 16,2 30,10"/><rect x="5" y="12" width="3" height="14"/><rect x="11" y="12" width="3" height="14"/><rect x="18" y="12" width="3" height="14"/><rect x="24" y="12" width="3" height="14"/><rect x="2" y="27" width="28" height="3"/></g></svg><p class="lorem">Lorem ipsum dolor sit amet, elit dolor sit consectetuer adipiscing elit. Maecenas porttitor congue massa.</p></div>
  <div class="m-item" style="top:288px"><svg class="m-icon" viewBox="0 0 32 32"><g fill="none" stroke="var(--blue)" stroke-width="3"><circle cx="16" cy="16" r="12"/><circle cx="16" cy="16" r="5"/></g></svg><p class="lorem">Lorem ipsum dolor sit amet, elit dolor sit consectetuer adipiscing elit. Maecenas porttitor congue massa.</p></div>
</div></section>

<!-- 6 Market opportunities feature -->
<section class="slide s6"><div class="frame">
  <svg class="bg" viewBox="0 0 626 352">
    <defs><linearGradient id="chipTone" x1="0" y1="0" x2="1" y2="0"><stop offset="0" stop-color="#2a1f7a"/><stop offset=".3" stop-color="#3a2a9a"/><stop offset="1" stop-color="#0f3f9a"/></linearGradient></defs>
    <rect width="626" height="352" fill="var(--paper)"/>
    <circle cx="555" cy="20" r="75" fill="var(--blush)"/>
    <circle cx="597" cy="35" r="20" fill="#fff" stroke="#f2c3c8" stroke-width="5"/>
    <rect y="70" width="626" height="192" fill="url(#chipTone)" role="img" aria-label="Glowing AI processor chip on a circuit background"/>
  </svg>
  <div class="brand" style="left:25px;top:17px"><span class="brand-dot"></span><span class="brand-name">Torvane</span></div>
  <p class="abs heading" style="right:25px;top:20px">MARKET OPPERTUNITIES</p>
  <p class="abs lorem" style="left:25px;top:290px;width:580px;font-size:10px">Lorem ipsum dolor sit amet, elit dolor sit consectetuer adipiscing elit. sit consectetuer adipiscing Lorem ipsum dolor sit amet, elit dolor sit consectetuer adipiscing elit. Maecenas sit consectetuer adipiscing sit consectetuer adipiscing Lorem ipsum dolor sit amet, elit dolor sit consectetuer adipiscing elit. sit consectetuer adipiscing</p>
</div></section>

<!-- 7 SWOT -->
<section class="slide s7"><div class="frame">
  <svg class="bg" viewBox="0 0 626 352">
    <rect width="626" height="352" fill="var(--paper)"/>
    <circle cx="570" cy="40" r="75" fill="var(--blush)"/>
  </svg>
  <div class="brand" style="left:25px;top:17px"><span class="brand-dot"></span><span class="brand-name">Torvane</span></div>
  <p class="abs heading" style="right:25px;top:22px">SWOT ANALYSIS</p>
  <div class="swot-col" style="left:0;background:var(--blue);color:var(--ink)"><h3>STRENTHS</h3><p>Lorem ipsum dolor sit amet, elit dolor sit consectetuer adipiscing elit. Maecenas porttitor congue massa. Lorem ipsum dolor sit amet, elit dolor sit consectetuer adipiscing elit. Maecenas porttitor congue massa.</p></div>
  <div class="swot-col" style="left:157px;background:var(--dark)"><h3>WEAKNESSES</h3><p>Lorem ipsum dolor sit amet, elit dolor sit consectetuer adipiscing elit. Maecenas porttitor congue massa. Lorem ipsum dolor sit amet, elit dolor sit consectetuer adipiscing elit. Maecenas porttitor congue massa.</p></div>
  <div class="swot-col" style="left:313px;background:var(--bright)"><h3>OPPORTUNITIES</h3><p>Lorem ipsum dolor sit amet, elit dolor sit consectetuer adipiscing elit. Maecenas porttitor congue massa. Lorem ipsum dolor sit amet, elit dolor sit consectetuer adipiscing elit. Maecenas porttitor congue massa.</p></div>
  <div class="swot-col" style="left:470px;background:var(--deep)"><h3>THREATS</h3><p>Lorem ipsum dolor sit amet, elit dolor sit consectetuer adipiscing elit. Maecenas porttitor congue massa. Lorem ipsum dolor sit amet, elit dolor sit consectetuer adipiscing elit. Maecenas porttitor congue massa.</p></div>
</div></section>

<!-- 8 Team -->
<section class="slide s8"><div class="frame">
  <svg class="bg" viewBox="0 0 626 352">
    <rect width="626" height="352" fill="var(--paper)"/>
    <circle cx="625" cy="140" r="85" fill="var(--blush)"/>
    <polygon points="180,18 280,18 302,43 280,68 180,68" fill="var(--deep)"/>
    <polygon points="285,18 370,18 392,43 370,68 285,68 307,43" fill="#ff6b6b"/>
    <polygon points="375,18 450,18 472,43 450,68 375,68 397,43" fill="#ff9a9a"/>
    <polygon points="455,18 510,18 532,43 510,68 455,68 477,43" fill="#ffc4c8"/>
    <rect x="178" y="68" width="3" height="215" fill="var(--bright)"/>
    <g fill="var(--dark)">
      <circle cx="77" cy="85" r="9"/><path d="M61,112 Q61,97 77,97 Q93,97 93,112 Z"/>
      <circle cx="77" cy="138" r="9"/><path d="M61,165 Q61,150 77,150 Q93,150 93,165 Z"/>
      <circle cx="77" cy="191" r="9"/><path d="M61,218 Q61,203 77,203 Q93,203 93,218 Z"/>
    </g>
    <polygon points="0,352 0,310 90,228 215,352" fill="var(--blue)"/>
    <polygon points="0,352 0,330 90,248 195,352" fill="var(--bright)"/>
    <polygon points="20,352 90,272 170,352" fill="var(--dark)"/>
    <polygon points="105,352 180,270 250,352" fill="var(--bright)"/>
    <polygon points="125,352 180,290 232,352" fill="var(--dark)"/>
  </svg>
  <div class="brand" style="left:25px;top:33px;gap:5px"><span class="brand-dot" style="width:20px;height:20px"></span><span class="brand-name" style="font-size:19px">Torvane</span></div>
  <p class="abs heading" style="left:217px;top:87px">TEAM</p>
  <div class="member" style="left:217px;top:130px"><p class="role">TITLE</p><p class="lorem">Lorem ipsum dolor sit amet, elit dolor sit consectetuer adipiscing elit. Maecenas porttitor congue massa.</p></div>
  <div class="member" style="left:392px;top:130px"><p class="role">TITLE</p><p class="lorem">Lorem ipsum dolor sit amet, elit dolor sit consectetuer adipiscing elit. Maecenas porttitor congue massa.</p></div>
  <div class="member" style="left:289px;top:238px"><p class="role">TITLE</p><p class="lorem">Lorem ipsum dolor sit amet, elit dolor sit consectetuer adipiscing elit. Maecenas porttitor congue massa.</p></div>
  <div class="member" style="left:464px;top:238px"><p class="role">TITLE</p><p class="lorem">Lorem ipsum dolor sit amet, elit dolor sit consectetuer adipiscing elit. Maecenas porttitor congue massa.</p></div>
</div></section>

<!-- 9 Financial analysis -->
<section class="slide s9"><div class="frame">
  <svg class="bg" viewBox="0 0 626 352">
    <rect width="626" height="352" fill="var(--blue)"/>
    <rect x="313" width="313" height="352" fill="var(--deep)"/>
    <rect x="313" width="27" height="352" fill="var(--bright)"/>
    <circle cx="290" cy="45" r="80" fill="#8fb6d8" opacity=".55"/>
    <g font-family="Poppins, sans-serif" font-size="8" fill="#fff" text-anchor="end">
      <text x="50" y="160">250</text><text x="50" y="186">200</text><text x="50" y="212">150</text>
      <text x="50" y="239">100</text><text x="50" y="265">50</text><text x="50" y="292">0</text>
    </g>
    <g fill="#fff">
      <rect x="79" y="172" width="12" height="117" rx="6"/>
      <rect x="121" y="222" width="12" height="67" rx="6"/>
      <rect x="164" y="150" width="12" height="139" rx="6"/>
      <rect x="206" y="188" width="12" height="101" rx="6"/>
      <rect x="248" y="188" width="12" height="101" rx="6"/>
    </g>
    <g fill="var(--bright)">
      <circle cx="85" cy="218" r="4"/><circle cx="127" cy="262" r="4"/><circle cx="170" cy="193" r="4"/><circle cx="212" cy="241" r="4"/><circle cx="254" cy="235" r="4"/>
    </g>
    <g font-family="Poppins, sans-serif" font-size="8" fill="#fff" text-anchor="middle">
      <text x="85" y="305">Goal 1</text><text x="127" y="305">Goal 2</text><text x="170" y="305">Goal 3</text><text x="212" y="305">Goal 4</text><text x="254" y="305">Goal 5</text>
    </g>
  </svg>
  <div class="brand" style="left:66px;top:40px"><span class="brand-dot"></span><span class="brand-name">Torvane</span></div>
  <p class="abs" style="left:370px;top:36px;width:200px;text-align:center;color:#fff;font-weight:700;font-size:14.5px;line-height:19px">FINANCIAL<br>ANALYSIS</p>
  <p class="abs lorem" style="left:365px;top:122px;width:210px;text-align:center;color:#fff">Lorem ipsum dolor sit amet, elit dolor sit consectetuer adipiscing elit. Maecenas porttitor congue massa. Lorem ipsum dolor sit amet, elit dolor sit consectetuer adipiscing elit. Maecenas porttitor congue massa. Lorem ipsum dolor sit amet, elit dolor sit consectetuer adipiscing elit.<br><br>Maecenas porttitor congue massa. Lorem ipsum dolor sit amet, elit dolor sit consectetuer adipiscing elit. Maecenas porttitor congue massa.</p>
</div></section>

<!-- 10 Thank you -->
<section class="slide s10"><div class="frame">
  <svg class="bg" viewBox="0 0 626 352">
    <rect width="626" height="352" fill="var(--dark)"/>
    <circle cx="40" cy="200" r="112" fill="#555"/>
    <polygon points="475,352 550,278 626,352" fill="var(--bright)"/>
    <polygon points="500,352 550,302 600,352" fill="var(--red)"/>
    <polygon points="520,352 550,322 580,352" fill="var(--dark)"/>
  </svg>
  <p class="abs thanks">THANK YOU</p>
</div></section>

</body>
</html>
```